Design a Flyer for Super Hero Day

Looking for a unique/cool flyer design for a kids super hero party.

I'll need an 8.5x11 flyer and a 4x6 matching in style image.

This should say: Fighting for Justice! Pursuing the Good! Striving for Awesome!

For any photos/images you need please use www.Pictovane.com I will purchase and attach any images for the winning designer. In the meantime, simply take a screen shot of the image you'd like to use, I understand the watermarks will be there, that's okay, we'll purchase the winning photos at the end.

Suggestions: Cool comic book style, maybe, mixed with a reality picture of a real kid?

I will need all photoshop work/source files in case there needs to be any edits, changes. There should be a space for a logo/day/date/time information. I appreciate if this can be incorporated INTO the design someway, and not just "added" if that makes sense.

Also, if you have questions post for clarification, I'll be quick to reply. Thank you :)

```html
<!DOCTYPE html>
<html lang="en">
<head>
<meta charset="utf-8">
<title>Super Hero Party Flyer</title>
<link rel="stylesheet" href="https://fonts.googleapis.com/css2?family=Bangers&family=Lilita+One&family=Pacifico&family=Oswald:wght@700&display=swap">
<style>
  :root {
    --orange-core: #d2712f;
    --orange-mid: #b4531f;
    --rust-edge: #6e2a0f;
    --comic-yellow: #f8d34c;
    --ink-brown: #3a1608;
    --hero-red: #c5202a;
    --cream: #f3e2b3;
    --cream-dark: #dcc38a;
    --tail-shade: #9c7b45;
    --night: #1a0d08;
  }
  html, body {
    margin: 0;
    padding: 0;
    overflow: hidden;
    background: #ffffff;
  }
  .flyer {
    position: relative;
    width: 928px;
    height: 1200px;
    overflow: hidden;
    background: radial-gradient(ellipse at 50% 45%, var(--orange-core) 0%, var(--orange-mid) 55%, var(--rust-edge) 100%);
  }
  .comic-collage {
    position: absolute;
    inset: 0;
    background: linear-gradient(160deg, rgba(120, 40, 10, 0.35) 0%, rgba(255, 170, 90, 0.12) 45%, rgba(90, 25, 5, 0.35) 100%);
  }
  .date-badge {
    position: absolute;
    left: 40px;
    top: 88px;
    width: 166px;
    height: 166px;
    border-radius: 50%;
    background: var(--night);
    display: flex;
    flex-direction: column;
    align-items: center;
    justify-content: center;
    font-family: "Bangers", sans-serif;
    color: var(--hero-red);
    -webkit-text-stroke: 1.5px var(--comic-yellow);
    transform: rotate(-8deg);
    line-height: 0.9;
  }
  .date-badge .month { font-size: 56px; letter-spacing: 1px; }
  .date-badge .day { font-size: 60px; }
  .date-badge .day sup { font-size: 28px; vertical-align: 24px; }
  .tagline {
    position: absolute;
    left: 208px;
    top: 72px;
    width: 680px;
    margin: 0;
    font-family: "Bangers", sans-serif;
    font-weight: 400;
    font-size: 62px;
    line-height: 56px;
    letter-spacing: 2px;
    color: var(--comic-yellow);
    text-shadow: 3px 3px 0 var(--ink-brown), -1px -1px 0 var(--ink-brown), 1px -1px 0 var(--ink-brown), -1px 1px 0 var(--ink-brown);
    transform: rotate(-7deg);
    transform-origin: left top;
  }
  .tagline span { display: block; white-space: nowrap; }
  .tagline .line-1 { margin-left: 4px; }
  .tagline .line-2 { margin-left: 36px; }
  .tagline .line-3 { margin-left: 6px; }
  .hero-frame {
    position: absolute;
    left: 165px;
    top: 230px;
    width: 618px;
    height: 618px;
  }
  .hero-photo {
    position: absolute;
    left: 209px;
    top: 274px;
    width: 530px;
    height: 530px;
    border-radius: 50%;
    background: linear-gradient(100deg, #3a1d10 0%, #e9b9a5 22%, #c9302a 40%, #b72a25 55%, #5fb6d8 72%, #c9302a 88%, #3a1d10 100%);
    opacity: 0.9;
  }
  .title-banner {
    position: absolute;
    left: 110px;
    top: 740px;
    width: 708px;
    height: 230px;
  }
  .title-super {
    position: absolute;
    left: 0;
    top: 798px;
    width: 928px;
    margin: 0;
    text-align: center;
    font-family: "Lilita One", sans-serif;
    font-weight: 400;
    font-size: 100px;
    line-height: 1;
    letter-spacing: 1px;
    color: var(--hero-red);
    text-shadow: 4px 4px 0 var(--ink-brown);
  }
  .title-party {
    position: absolute;
    left: 0;
    top: 890px;
    width: 928px;
    text-align: center;
    font-family: "Pacifico", cursive;
    font-size: 92px;
    line-height: 1;
    color: var(--cream);
    -webkit-text-stroke: 3px var(--night);
    paint-order: stroke fill;
    text-shadow: 4px 4px 0 var(--night);
  }
  .ticket {
    position: absolute;
    left: 0;
    top: 1040px;
    width: 928px;
    margin: 0;
    text-align: center;
    font-family: "Oswald", sans-serif;
    font-weight: 700;
    font-size: 24px;
    line-height: 1;
    letter-spacing: 1px;
    color: var(--ink-brown);
  }
  .logo-slot {
    position: absolute;
    left: 0;
    top: 1126px;
    width: 928px;
    margin: 0;
    text-align: center;
    font-family: "Lilita One", sans-serif;
    font-size: 40px;
    line-height: 1;
    color: var(--comic-yellow);
  }
</style>
</head>
<body>
  <main class="flyer">
    <div class="comic-collage" role="img" aria-label="Faded collage of vintage comic book covers in orange tones"></div>

    <div class="date-badge">
      <span class="month">JULY</span>
      <span class="day">00<sup>TH</sup></span>
    </div>

    <h2 class="tagline">
      <span class="line-1">Fighting for Justice!</span>
      <span class="line-2">Pursuing the Good!</span>
      <span class="line-3">Striving for Awesome!</span>
    </h2>

    <svg class="hero-frame" viewBox="0 0 618 618" aria-hidden="true">
      <defs>
        <radialGradient id="burst" cx="50%" cy="50%" r="50%">
          <stop offset="0%" stop-color="#7a4a28"/>
          <stop offset="70%" stop-color="#4a2612"/>
          <stop offset="100%" stop-color="#24110a"/>
        </radialGradient>
      </defs>
      <circle cx="309" cy="309" r="305" fill="var(--cream)"/>
      <circle cx="309" cy="309" r="294" fill="none" stroke="var(--ink-brown)" stroke-width="2" stroke-dasharray="5 4"/>
      <circle cx="309" cy="309" r="278" fill="url(#burst)"/>
    </svg>

    <div class="hero-photo" role="img" aria-label="Photo of two children in masks, red capes and red gloves striking superhero poses"></div>

    <svg class="title-banner" viewBox="0 0 708 230" aria-hidden="true">
      <polygon points="0,60 70,60 70,215 0,215 40,137" fill="var(--cream-dark)"/>
      <polygon points="708,60 638,60 638,215 708,215 668,137" fill="var(--cream-dark)"/>
      <polygon points="45,180 70,215 70,180" fill="var(--tail-shade)"/>
      <polygon points="663,180 638,215 638,180" fill="var(--tail-shade)"/>
      <path d="M45,10 Q354,-8 663,10 L663,182 Q354,164 45,182 Z" fill="var(--cream)" stroke="var(--cream-dark)" stroke-width="3"/>
    </svg>

    <h1 class="title-super">SUPER HERO</h1>
    <div class="title-party">Party</div>

    <p class="ticket">TICKET: ??</p>
    <p class="logo-slot">YOUR LOGO</p>
  </main>
</body>
</html>
```